Bolvarin Incorporated

Bolvarin is a business that provides consulting, and manages and supplies trades persons in the construction and heavy industries sector. We build, do maintenance, install machinery, and can manage projects or jobs. Would like or prefer more clean, classic designs. Blacks/greys, but open to almost anything.

Target Market(s)

Industrial/Construction/Manufacturing

Industry/Entity Type

Construction Company

Contact Information for Business Card

Clean, business name on the front, possibly have the details on the back, but open to any ideas.

Logo Text

We currently do not have a slogan, open to ideas

Font styles to use
Serif
Sans Serif

Colors

Designer to choose colors to be used in the design.

Requirements
Should not have
• the oval is not my logo, was just an idea. please don't send 20 designs with the oval

```html
<!DOCTYPE html>
<html lang="en">
<head>
<meta charset="utf-8">
<title>Bolvarin Incorporated — Business Card</title>
<link href="https://fonts.googleapis.com/css2?family=Oswald:wght@500&family=Work+Sans:wght@400&display=swap" rel="stylesheet">
<style>
  :root {
    --backdrop: #121212;
    --card-dark: #1a1a1a;
    --card-light: #262626;
    --ink: #f2f2f2;
    --brand-ink: #c9c9c9;
  }
  * { margin: 0; padding: 0; box-sizing: border-box; }
  html, body {
    width: 1200px;
    height: 900px;
    overflow: hidden;
    background: var(--backdrop);
  }
  .canvas {
    position: relative;
    width: 1200px;
    height: 900px;
    display: flex;
    flex-direction: column;
    align-items: center;
    justify-content: center;
    gap: 40px;
  }
  .card {
    position: relative;
    width: 680px;
    height: 388px;
    background: linear-gradient(135deg, var(--card-dark) 0%, var(--card-light) 70%, var(--card-dark) 100%);
    box-shadow: 0 10px 30px rgba(0, 0, 0, 0.6);
  }
  .card-front {
    display: flex;
    align-items: center;
    justify-content: center;
  }
  .brand-name {
    font-family: "Work Sans", sans-serif;
    font-weight: 400;
    font-size: 52px;
    letter-spacing: 2px;
    color: var(--brand-ink);
  }
  .holder {
    position: absolute;
    left: 70px;
    top: 140px;
    text-align: right;
  }
  .holder-name {
    font-family: "Oswald", sans-serif;
    font-weight: 500;
    font-size: 40px;
    letter-spacing: 1px;
    line-height: 1.1;
    color: var(--ink);
  }
  .holder-title {
    font-family: "Work Sans", sans-serif;
    font-size: 19px;
    letter-spacing: 1px;
    color: var(--ink);
  }
  .divider {
    position: absolute;
    left: 345px;
    top: 150px;
    width: 2px;
    height: 82px;
    background: var(--ink);
  }
  .contact-list {
    position: absolute;
    left: 372px;
    top: 146px;
    list-style: none;
    font-family: "Work Sans", sans-serif;
    font-size: 19px;
    letter-spacing: 1px;
    color: var(--ink);
  }
  .contact-list li {
    display: flex;
    align-items: center;
    gap: 8px;
    height: 29px;
  }
  .contact-icon {
    width: 13px;
    height: 13px;
    flex: none;
  }
  .address {
    position: absolute;
    left: 70px;
    bottom: 62px;
    font-family: "Work Sans", sans-serif;
    font-size: 19px;
    letter-spacing: 1.5px;
    color: var(--ink);
  }
</style>
</head>
<body>
<main class="canvas">
  <section class="card card-front">
    <span class="brand-name">Bolvarin</span>
  </section>

  <section class="card card-back">
    <div class="holder">
      <h1 class="holder-name">DORIAN WALSH</h1>
      <p class="holder-title">Director</p>
    </div>
    <span class="divider"></span>
    <ul class="contact-list">
      <li>
        <svg class="contact-icon" viewBox="0 0 16 16" fill="none" stroke="#f2f2f2" stroke-width="1.5">
          <path d="M4 1.5 L6 5 L4.5 6.5 C5.5 8.5 7.5 10.5 9.5 11.5 L11 10 L14.5 12 L13 14.5 C7 14 2 9 1.5 3 Z"/>
        </svg>
        403.555.0142
      </li>
      <li>
        <svg class="contact-icon" viewBox="0 0 16 16" fill="none" stroke="#f2f2f2" stroke-width="1.5">
          <rect x="1" y="3" width="14" height="10"/>
          <path d="M1 3 L8 9 L15 3"/>
        </svg>
        info@bolvarinco.ca
      </li>
      <li>
        <svg class="contact-icon" viewBox="0 0 16 16" fill="none" stroke="#f2f2f2" stroke-width="1.2">
          <circle cx="8" cy="8" r="6.5"/>
          <ellipse cx="8" cy="8" rx="3" ry="6.5"/>
          <path d="M1.5 8 H14.5 M2.5 4.5 H13.5 M2.5 11.5 H13.5"/>
        </svg>
        www.bolvarinco.ca
      </li>
    </ul>
    <p class="address">1480 Hollowmere Drive Cedar Point, FL 32801</p>
  </section>
</main>
</body>
</html>
```